Business cards real estate company

We need a design for a business card. It is a company that specializes in real estate sales. There should be space for a photo of the respective employee as well as the website and telephone number on it. Design should be noble, innovative.

Contact Information for Business Card

Website, Name, Position, Telefonnummer

Requirements
Must have
• Photo, logo

```html
<!DOCTYPE html>
<html lang="en">
<head>
<meta charset="utf-8">
<title>Domivera – Business Card</title>
<link href="https://fonts.googleapis.com/css2?family=Poppins:wght@300;400;600;700&display=swap" rel="stylesheet">
<style>
  :root {
    --page: #d9d9d9;
    --card: #121212;
    --green: #6cc72e;
    --line: #b5e61d;
    --text-grey: #bdbdbd;
    --photo-top: #6a6a6a;
    --photo-bottom: #4e4e4e;
  }
  * { margin: 0; padding: 0; box-sizing: border-box; }
  html, body { width: 1200px; height: 800px; overflow: hidden; }
  body {
    background: var(--page);
    font-family: "Poppins", sans-serif;
    display: flex;
    flex-direction: column;
    align-items: center;
    justify-content: center;
    gap: 40px;
  }
  .card {
    position: relative;
    width: 620px;
    height: 354px;
    background: var(--card);
    box-shadow: 0 10px 24px rgba(0,0,0,0.25);
    overflow: hidden;
  }

  /* Contact side */
  .brand-square {
    position: absolute;
    left: 72px; top: 118px;
    width: 44px; height: 44px;
    background: var(--green);
  }
  .divider {
    position: absolute;
    left: 190px; right: 30px; top: 214px;
    height: 1px;
    background: var(--line);
  }
  .person {
    position: absolute;
    right: 30px; top: 150px;
    text-align: right;
  }
  .person-name {
    color: var(--green);
    font-weight: 600;
    font-size: 25px;
    line-height: 1.1;
  }
  .person-role {
    color: var(--text-grey);
    font-weight: 300;
    font-size: 14px;
    line-height: 1.3;
  }
  .address {
    position: absolute;
    right: 30px; top: 226px;
    text-align: right;
    color: var(--text-grey);
    font-weight: 300;
    font-size: 13px;
    line-height: 1.5;
  }
  .contact-list {
    position: absolute;
    left: 190px; top: 228px;
    list-style: none;
    color: var(--text-grey);
    font-weight: 300;
    font-size: 13px;
    line-height: 1.5;
  }
  .contact-list li { display: flex; align-items: center; gap: 8px; }
  .contact-list svg { width: 11px; height: 11px; flex: none; }

  /* Brand side */
  .brand-name {
    position: absolute;
    left: 52px; top: 196px;
    color: var(--green);
    font-weight: 700;
    font-size: 58px;
    letter-spacing: 0.5px;
    line-height: 1;
  }
  .employee-photo {
    position: absolute;
    right: 0; top: 0;
    width: 250px; height: 100%;
    background: linear-gradient(180deg, var(--photo-top), var(--photo-bottom));
  }
</style>
</head>
<body>

  <section class="card card-contact">
    <div class="brand-square"></div>

    <div class="person">
      <p class="person-name">Daniel Hart</p>
      <p class="person-role">President</p>
    </div>

    <div class="divider"></div>

    <address class="address">
      1420 Alder Street<br>
      Juneau, Alaska 99801<br>
      www.domivera.com
    </address>

    <ul class="contact-list">
      <li>
        <svg viewBox="0 0 12 12" aria-hidden="true"><path d="M2 1h3l1 3-1.5 1a6 6 0 0 0 2.5 2.5L8 6l3 1v3a1 1 0 0 1-1 1A9 9 0 0 1 1 2a1 1 0 0 1 1-1z" fill="var(--green)"/></svg>
        555-214-7302
      </li>
      <li>
        <svg viewBox="0 0 12 12" aria-hidden="true"><rect x="3" y="0.8" width="6" height="10.4" rx="1" fill="none" stroke="var(--green)" stroke-width="1.4"/></svg>
        555-418-6091
      </li>
      <li>
        <svg viewBox="0 0 12 12" aria-hidden="true"><rect x="0.7" y="2" width="10.6" height="8" fill="none" stroke="var(--green)" stroke-width="1.4"/><path d="M1 2.5 6 6.5l5-4" fill="none" stroke="var(--green)" stroke-width="1.4"/></svg>
        hello@domivera.com
      </li>
    </ul>
  </section>

  <section class="card card-brand">
    <div class="employee-photo" role="img" aria-label="Portrait photo of the employee"></div>
    <p class="brand-name">Domivera</p>
  </section>

</body>
</html>
```